Grace Chapel Lakemont, MS needs a Business Card design

We are in the process of rebranding our church with a new logo with a fresh appeal to younger families moving into our community and joining our church. We are in need of a new business card design and would like to see 2 sided designs that incorporate the web color 00cccc.

We would like to have our logo, church name (grace chapel lakemont) and our what we are about (gather.grow.go.) in addition to the following information:
Name: Dr. Steven Haldane
Title: Teaching Pastor
Phone: 6014973512
Email: shaldane@gclakemont.org
Website: www.gclakemont.org
Address: 742 N Willow Avenue Brandon, MS 39158

Target Market(s)

Brandon, MS is a bedroom community outside of Jackson that is experiencing exponential growth with young professionals/young families moving in. We are making a lot of changes to reach this demographic while still honoring and continuing to reach those who have lived here for a while.

Industry/Entity Type

Church

Contact Information for Business Card

Grace Chapel Lakemont - gather.grow.go.
Dr. Steven Haldane
Teaching Pastor
6014973512
shaldane@gclakemont.org
www.gclakemont.org
742 N Willow Avenue
Brandon, MS 39158

Font styles to use
Sans Serif

```html
<!DOCTYPE html>
<html lang="en">
<head>
<meta charset="utf-8">
<title>Grace Chapel Lakemont – Business Card</title>
<link href="https://fonts.googleapis.com/css2?family=Barlow:wght@400;600&family=Work+Sans:wght@400;500&display=swap" rel="stylesheet">
<style>
  :root {
    --stage: #e9e9ea;
    --slate: #6b6c70;
    --slate-soft: #8a8b8f;
    --teal: #12a79d;
    --teal-light: #8fd3cc;
    --paper: #ffffff;
    --ink: #5f6064;
  }
  * { box-sizing: border-box; margin: 0; padding: 0; }
  html, body { width: 1200px; height: 930px; overflow: hidden; background: var(--stage); }
  .canvas { position: relative; width: 1200px; height: 930px; }

  .card {
    position: absolute;
    left: 290px;
    width: 620px;
    height: 354px;
    border-radius: 18px;
    overflow: hidden;
    box-shadow: 0 6px 18px rgba(0,0,0,.18);
  }

  /* Back */
  .card--back { top: 60px; background: var(--slate); }
  .back-brand {
    position: absolute; right: 56px; top: 176px;
    display: flex; flex-direction: column; align-items: flex-end;
  }
  .back-wordmark { display: flex; align-items: center; gap: 14px; white-space: nowrap; }
  .back-wordmark__dot { width: 14px; height: 14px; border-radius: 50%; background: var(--teal-light); }
  .back-wordmark__name {
    font-family: "Barlow", sans-serif; font-weight: 400;
    font-size: 34px; line-height: 40px; letter-spacing: 1px; color: var(--paper); text-transform: uppercase;
  }
  .back-tagline {
    margin-top: 6px;
    font-family: "Work Sans", sans-serif; font-weight: 500;
    font-size: 18px; letter-spacing: 1.5px; color: var(--paper); white-space: nowrap;
  }

  /* Front */
  .card--front { top: 516px; background: var(--paper); }
  .front-wordmark {
    position: absolute; left: 36px; top: 84px;
    display: flex; align-items: center; gap: 10px; white-space: nowrap;
  }
  .front-wordmark__dot { width: 12px; height: 12px; border-radius: 50%; background: var(--slate-soft); }
  .front-wordmark__name {
    font-family: "Barlow", sans-serif; font-weight: 400;
    font-size: 20px; letter-spacing: .6px; color: var(--slate-soft); text-transform: uppercase;
  }
  .person { position: absolute; right: 34px; top: 42px; text-align: right; white-space: nowrap; }
  .person__name { font-family: "Work Sans", sans-serif; font-weight: 500; font-size: 27px; line-height: 34px; color: var(--teal); }
  .person__title { font-family: "Work Sans", sans-serif; font-size: 16px; color: var(--ink); margin-top: 2px; }
  .rule { position: absolute; left: 36px; right: 34px; top: 124px; height: 1.5px; background: var(--teal); }
  .address {
    position: absolute; right: 34px; top: 142px; text-align: right; white-space: nowrap; font-style: normal;
    font-family: "Work Sans", sans-serif; font-size: 15px; line-height: 1.4; color: var(--ink);
  }
  .contacts { position: absolute; left: 36px; top: 146px; list-style: none; }
  .contacts li {
    display: flex; align-items: center; gap: 12px; white-space: nowrap;
    font-family: "Work Sans", sans-serif; font-size: 16px; line-height: 26px; color: var(--ink);
  }
  .contacts svg { width: 12px; height: 12px; flex: none; }
  .front-band { position: absolute; left: 0; bottom: 0; width: 620px; height: 110px; }
</style>
</head>
<body>
<main class="canvas">

  <section class="card card--back" aria-label="Card back">
    <div class="back-brand">
      <div class="back-wordmark">
        <span class="back-wordmark__dot"></span>
        <span class="back-wordmark__name">Grace Chapel Lakemont</span>
      </div>
      <p class="back-tagline">gather.grow.go.</p>
    </div>
  </section>

  <section class="card card--front" aria-label="Card front">
    <div class="front-wordmark">
      <span class="front-wordmark__dot"></span>
      <span class="front-wordmark__name">Grace Chapel Lakemont</span>
    </div>

    <div class="person">
      <p class="person__name">Dr. Steven Haldane</p>
      <p class="person__title">Teaching Pastor</p>
    </div>
    <div class="rule"></div>

    <address class="address">
      742 N Willow Avenue<br>Brandon, MS 39158
    </address>

    <ul class="contacts">
      <li>
        <svg viewBox="0 0 12 12"><path d="M2.5 1 L4.5 1 L5.3 3.6 L4 4.6 Q5 7 7.4 8 L8.4 6.7 L11 7.5 L11 9.5 Q10.5 11 9 11 Q1 10 1 3 Q1 1.5 2.5 1Z" fill="var(--teal)"/></svg>
        6014973512
      </li>
      <li>
        <svg viewBox="0 0 12 12"><rect x="1" y="2.5" width="10" height="7" rx="1" fill="none" stroke="var(--teal)" stroke-width="1.3"/><path d="M1.5 3 L6 6.6 L10.5 3" fill="none" stroke="var(--teal)" stroke-width="1.3"/></svg>
        shaldane@gclakemont.org
      </li>
      <li>
        <svg viewBox="0 0 12 12"><circle cx="6" cy="6" r="5" fill="var(--teal)"/><path d="M1 6 H11 M6 1 Q3 6 6 11 M6 1 Q9 6 6 11" fill="none" stroke="#fff" stroke-width=".8"/></svg>
        www.gclakemont.org
      </li>
    </ul>

    <svg class="front-band" viewBox="0 0 620 110" preserveAspectRatio="none" aria-hidden="true">
      <path d="M0 92 L430 92 Q448 92 462 80 L500 50 Q520 36 545 36 L620 36 L620 110 L0 110 Z" fill="var(--teal)"/>
      <path d="M0 84 L425 84 Q440 84 452 74 L470 60 L474 64 L456 78 Q444 88 428 88 L0 88 Z" fill="var(--slate)"/>
    </svg>
  </section>

</main>
</body>
</html>
```